Thornbury Lettings Managment Ltd website

Need a website To inform people/clients of the services we provide. 5 pages total with a local feel. Bristol, UK. I have logo artwork already is like the look based on
incorporate the artwork attached for theme, feel and colours fonts info etc

To best describe the business have a brief look at www.fernwickhomes.example.co.uk which is a local firm offering the same services. This is for your ref only and not to be copied.

Target Market(s)

Property Investors/Landlords

Coding

Coded - Design and coding required

Number of Pages Required

5+ page

Colors
0392cd
f68d4d

Requirements
Must have
• local feel. Possibly using some local architecture or historic landmarks etc. This is fexible.
• most also be mobile device compatible
Nice to have
• the membership logos - files attached: KTB, DWF, GMV and safehold-example.co.uk

```html
<!DOCTYPE html>
<html lang="en">
<head>
<meta charset="utf-8">
<title>Thornbury Lettings Managment Ltd</title>
<link href="https://fonts.googleapis.com/css2?family=Cabin:wght@400;500;600&family=Open+Sans:wght@400;600;700&display=swap" rel="stylesheet">
<style>
:root{
  --navy:#1f4a5f;
  --orange:#f68d4d;
  --blue:#0392cd;
  --text:#6b6f72;
  --light:#f2f3f2;
  --white:#ffffff;
  --dark:#1d2125;
}
*{margin:0;padding:0;box-sizing:border-box}
html,body{width:1200px;height:4369px;overflow:hidden}
body{font-family:"Open Sans",Arial,sans-serif;color:var(--text);background:var(--white)}
.page{position:relative;width:1200px;height:623px;overflow:hidden}
.page.hero{height:626px}
.page.footer{height:628px}
.page.alt{background:var(--light)}
.sidebar{position:absolute;left:0;top:0;width:292px;height:100%;
  background:linear-gradient(180deg,#f3f3f3 0,#d8d9da 10%,#7c8084 24%,#3a3f44 40%,#1d2125 100%)}
.brand{position:absolute;left:42px;top:62px;display:flex;align-items:center;gap:10px}
.brand-mark{width:34px;height:34px;background:var(--navy)}
.brand-name{font-family:"Cabin",sans-serif;font-weight:600;font-size:17px;line-height:1.1;color:var(--navy);width:190px}
.nav{position:absolute;left:112px;top:202px;list-style:none}
.nav li{height:44px;font-size:15px;color:var(--white);font-weight:600}
.nav li.active{color:var(--orange)}
.photo{position:absolute}
.hero-photo{left:292px;top:0;width:908px;height:626px;
  background:linear-gradient(180deg,#6fa6d4 0,#a9c9e2 30%,#c9a27a 48%,#7e7466 62%,#3d5a6e 78%,#22394a 100%)}
.hero-title{position:absolute;left:342px;top:48px;font-family:"Cabin",sans-serif;font-weight:500;font-size:54px;color:var(--white)}
.hero-sub{position:absolute;right:56px;top:118px;font-family:"Cabin",sans-serif;font-size:25px;color:var(--navy);font-weight:500}
.heading{position:absolute;left:292px;width:908px;top:52px;text-align:center;font-family:"Cabin",sans-serif;font-weight:400;font-size:44px;color:var(--navy)}
.intro{position:absolute;left:340px;width:812px;top:124px;text-align:center;font-size:16px;line-height:26px}
.side-text{position:absolute;font-size:14px;line-height:24px}
.lead{color:var(--orange);font-weight:700;font-size:15px;line-height:26px;margin-bottom:12px}
.benefits-title{color:var(--orange);font-weight:700;font-size:15px;margin-bottom:22px}
.benefits{list-style:none}
.benefits li{position:relative;padding-left:26px;margin-bottom:26px;font-size:14px;line-height:23px}
.benefits li::before{content:"";position:absolute;left:0;top:7px;width:10px;height:10px;border-radius:50%;background:var(--blue)}
.card{position:absolute;top:228px;width:232px}
.card-img{height:118px;border:6px solid var(--white);box-shadow:0 1px 3px rgba(0,0,0,.2)}
.card-label{position:relative;margin:-30px 0 0 -6px;width:210px;height:28px;background:var(--navy);color:var(--white);font-weight:700;font-size:13px;line-height:28px;padding-left:14px}
.card p{margin-top:30px;font-size:12.5px;line-height:19px}
.read-more{margin-top:26px;display:flex;align-items:center;gap:10px;font-size:12px;color:var(--orange)}
.read-more span.dot{width:20px;height:20px;background:var(--navy)}
.frame{border:1px solid #cfd2d4}
.footer-bg{position:absolute;left:292px;top:0;width:908px;height:628px;
  background:linear-gradient(180deg,#0f1a24 0,#1e3446 40%,#2b4356 70%,#14202a 100%)}
.badges{position:absolute;left:350px;top:52px;width:790px;height:96px;background:var(--white);display:flex;align-items:center;justify-content:space-around}
.badge{background:#d7dde2}
.col-title{position:absolute;top:198px;color:var(--white);font-weight:700;font-size:17px}
.contact-list{position:absolute;left:350px;top:262px;list-style:none;color:var(--white);font-size:13px}
.contact-list li{display:flex;gap:10px;margin-bottom:44px;line-height:19px}
.contact-list .label{color:var(--orange);width:70px}
.contact-list svg{flex:none;margin-top:2px}
.socials{position:absolute;left:362px;top:402px;display:flex;gap:16px}
.socials span{width:26px;height:26px;border-radius:50%;background:var(--white)}
.field{position:absolute;left:612px;width:241px;height:40px;background:var(--white);font-size:12px;color:#8a8d90;padding:10px 10px}
.submit{position:absolute;left:612px;top:493px;width:241px;height:36px;background:var(--orange);color:var(--white);font-weight:700;font-size:15px;text-align:center;line-height:36px}
.map{position:absolute;left:903px;top:178px;width:247px;height:305px;background:linear-gradient(135deg,#e6e2d8,#cfd8cf)}
.map-brand{position:absolute;left:920px;top:190px;display:flex;align-items:center;gap:8px}
.map-brand .brand-mark{width:26px;height:26px}
.map-brand .brand-name{font-size:14px;width:180px}
.map-link{position:absolute;left:960px;top:496px;font-size:12px;color:var(--orange)}
.copyright{position:absolute;left:292px;top:590px;width:908px;height:38px;background:#0d151c;color:#9aa3aa;font-size:12px;text-align:center;line-height:38px}
</style>
</head>
<body>

<section class="page hero">
  <div class="sidebar">
    <div class="brand" style="top:40px"><span class="brand-mark"></span><span class="brand-name">Thornbury Lettings Managment Ltd</span></div>
    <ul class="nav"><li class="active">Home</li><li>About Thornbury</li><li>What We Do</li><li>Landlords</li><li>Tenants</li><li>Agencies</li><li>Contact Us</li></ul>
  </div>
  <div class="photo hero-photo" role="img" aria-label="Photograph of a modern Bristol harbourside apartment block reflected in the water"></div>
  <h1 class="hero-title">Thornbury Lettings Management</h1>
  <p class="hero-sub">The Great Estates Management In Your Locality</p>
</section>

<section class="page">
  <div class="sidebar">
    <div class="brand"><span class="brand-mark"></span><span class="brand-name">Thornbury Lettings Managment Ltd</span></div>
    <ul class="nav" style="top:238px"><li>Home</li><li class="active">About Thornbury</li><li>What We Do</li><li>Landlords</li><li>Tenants</li><li>Agencies</li><li>Contact Us</li></ul>
  </div>
  <h2 class="heading">About Thornbury</h2>
  <p class="intro">Lorem Ipsum is simply dummy text of the printing and typesetting industry. Lorem Ipsum has been the industry's standard dummy text ever since the 1500s.</p>
  <div class="photo" style="left:346px;top:228px;width:305px;height:320px;background:linear-gradient(135deg,#8b7b6b,#b9b2a6 45%,#6d7f8e)" role="img" aria-label="Collage of four photographs of historic Bristol buildings and landmarks"></div>
  <div class="side-text" style="left:702px;top:225px;width:410px">
    <p class="lead">Phasellus nec turpis mattis, porttitor lacus ut, gravida arcu. Phasellus bibendum semper nulla dapibus in.</p>
    <p>Sed semper, nibh ac porta commodo, eros dui efficitur risus, a elementum augue elit at erat. Suspendisse imperdiet ut nibh a condimentum. Suspendisse molestie sapien sit amet leo mattis hendrerit sit amet in leo. Vivamus gravida lectus purus. Donec sagittis hendrerit elit. Vivamus mollis, lectus ac tempor finibus, metus ex dapibus nunc, eget pellentesque felis quam eget ligula. Donec interdum non nunc nec feugiat. Etiam a erat pulvinar, luctus ex et, laoreet ante. Vivamus varius volutpat bibendum. Proin lobortis magna sed elit iaculis, nec congue metus mattis.</p>
  </div>
</section>

<section class="page alt">
  <div class="sidebar">
    <div class="brand"><span class="brand-mark"></span><span class="brand-name">Thornbury Lettings Managment Ltd</span></div>
    <ul class="nav" style="top:196px"><li>Home</li><li>About Thornbury</li><li class="active">What We Do</li><li>Landlords</li><li>Tenants</li><li>Agencies</li><li>Contact Us</li></ul>
  </div>
  <h2 class="heading">What We Do</h2>
  <p class="intro">Lorem Ipsum is simply dummy text of the printing and typesetting industry. Lorem Ipsum has been the industry's standard dummy text ever since the 1500s.</p>
  <div class="card" style="left:352px">
    <div class="card-img" style="background:linear-gradient(135deg,#2b7fc0,#8cc1e6)" role="img" aria-label="Illustration of a house held in a hand"></div>
    <div class="card-label">Good With Management</div>
    <p>Donec egestas vitae mauris hendrerit ing euismod. Vestibulum vehicula vitae dum sodales interdum. Etiam a erat pulvinar, luctus ex et, laoreet ante. Lorem ipsum dolor sit amet, consectetur adipiscing elit.</p>
    <div class="read-more"><span class="dot"></span>Read More...</div>
  </div>
  <div class="card" style="left:618px">
    <div class="card-img" style="background:linear-gradient(135deg,#c9a15a,#efe0bf)" role="img" aria-label="Photograph of stacked coins"></div>
    <div class="card-label">Good With Finance</div>
    <p>Donec egestas vitae mauris hendrerit ing euismod. Vestibulum vehicula vitae dum sodales interdum. Etiam a erat pulvinar, luctus ex et, laoreet ante. Lorem ipsum dolor sit amet, consectetur adipiscing elit.</p>
    <div class="read-more"><span class="dot"></span>Read More...</div>
  </div>
  <div class="card" style="left:882px">
    <div class="card-img" style="background:linear-gradient(135deg,#9a4b3f,#d8c2b3)" role="img" aria-label="Photograph of a maintenance worker on a house"></div>
    <div class="card-label">Good With Maintenance</div>
    <p>Donec egestas vitae mauris hendrerit ing euismod. Vestibulum vehicula vitae dum sodales interdum. Etiam a erat pulvinar, luctus ex et, laoreet ante. Lorem ipsum dolor sit amet, consectetur adipiscing elit.</p>
    <div class="read-more"><span class="dot"></span>Read More...</div>
  </div>
</section>

<section class="page">
  <div class="sidebar">
    <div class="brand"><span class="brand-mark"></span><span class="brand-name">Thornbury Lettings Managment Ltd</span></div>
    <ul class="nav" style="top:196px"><li>Home</li><li>About Thornbury</li><li>What We Do</li><li class="active">Landlords</li><li>Tenants</li><li>Agencies</li><li>Contact Us</li></ul>
  </div>
  <h2 class="heading">Landlords</h2>
  <p class="intro">Lorem Ipsum is simply dummy text of the printing and typesetting industry. Lorem Ipsum has been the industry's standard dummy text ever since the 1500s.</p>
  <div class="photo frame" style="left:346px;top:228px;width:308px;height:320px;background:linear-gradient(135deg,#d9c6a8,#a88f73 55%,#6f8aa0)" role="img" aria-label="Photograph of a landlord handing house keys to new tenants"></div>
  <div class="side-text" style="left:702px;top:232px;width:410px">
    <p class="benefits-title">We give the following benefits to landlords:</p>
    <ul class="benefits"><li>Lorem ipsum dolor sit amet, consectetur adipiscing elit. Sac lorem et mauris volutpat pretium.</li><li>Lorem ipsum dolor sit amet, consectetur adipiscing elit. Sac lorem et mauris volutpat pretium.</li><li>Lorem ipsum dolor sit amet, consectetur adipiscing elit. Sac lorem et mauris volutpat pretium.</li><li>Lorem ipsum dolor sit amet, consectetur adipiscing elit. Sac lorem et mauris volutpat pretium.</li></ul>
  </div>
</section>

<section class="page alt">
  <div class="sidebar">
    <div class="brand"><span class="brand-mark"></span><span class="brand-name">Thornbury Lettings Managment Ltd</span></div>
    <ul class="nav" style="top:196px"><li>Home</li><li>About Thornbury</li><li>What We Do</li><li>Landlords</li><li class="active">Tenants</li><li>Agencies</li><li>Contact Us</li></ul>
  </div>
  <h2 class="heading">Tenants</h2>
  <p class="intro">Lorem Ipsum is simply dummy text of the printing and typesetting industry. Lorem Ipsum has been the industry's standard dummy text ever since the 1500s.</p>
  <div class="side-text" style="left:346px;top:222px;width:420px">
    <p class="benefits-title">We give the following benefits to tenants:</p>
    <ul class="benefits"><li>Lorem ipsum dolor sit amet, consectetur adipiscing elit. Sac lorem et mauris volutpat pretium.</li><li>Lorem ipsum dolor sit amet, consectetur adipiscing elit. Sac lorem et mauris volutpat pretium.</li><li>Lorem ipsum dolor sit amet, consectetur adipiscing elit. Sac lorem et mauris volutpat pretium.</li><li>Lorem ipsum dolor sit amet, consectetur adipiscing elit. Sac lorem et mauris volutpat pretium.</li></ul>
  </div>
  <div class="photo frame" style="left:815px;top:222px;width:306px;height:320px;background:linear-gradient(135deg,#e6e8ea,#b7bdc2 50%,#7d6a5e)" role="img" aria-label="Photograph of a happy couple in their new rented home"></div>
</section>

<section class="page">
  <div class="sidebar">
    <div class="brand"><span class="brand-mark"></span><span class="brand-name">Thornbury Lettings Managment Ltd</span></div>
    <ul class="nav" style="top:196px"><li>Home</li><li>About Thornbury</li><li>What We Do</li><li>Landlords</li><li>Tenants</li><li class="active">Agencies</li><li>Contact Us</li></ul>
  </div>
  <h2 class="heading">Agencies</h2>
  <p class="intro">Lorem Ipsum is simply dummy text of the printing and typesetting industry. Lorem Ipsum has been the industry's standard dummy text ever since the 1500s.</p>
  <div class="photo frame" style="left:346px;top:228px;width:308px;height:320px;background:linear-gradient(135deg,#c7a785,#e6d9c6 50%,#7f95a8)" role="img" aria-label="Photograph of an agent meeting a client across a desk"></div>
  <div class="side-text" style="left:702px;top:232px;width:410px">
    <p class="benefits-title">We give the following benefits to agencies:</p>
    <ul class="benefits"><li>Lorem ipsum dolor sit amet, consectetur adipiscing elit. Sac lorem et mauris volutpat pretium.</li><li>Lorem ipsum dolor sit amet, consectetur adipiscing elit. Sac lorem et mauris volutpat pretium.</li><li>Lorem ipsum dolor sit amet, consectetur adipiscing elit. Sac lorem et mauris volutpat pretium.</li><li>Lorem ipsum dolor sit amet, consectetur adipiscing elit. Sac lorem et mauris volutpat pretium.</li></ul>
  </div>
</section>

<section class="page footer">
  <div class="sidebar">
    <div class="brand"><span class="brand-mark"></span><span class="brand-name">Thornbury Lettings Managment Ltd</span></div>
    <ul class="nav" style="top:196px"><li>Home</li><li>About Thornbury</li><li>What We Do</li><li>Landlords</li><li>Tenants</li><li>Agencies</li><li class="active">Contact Us</li></ul>
  </div>
  <div class="footer-bg" role="img" aria-label="Dark evening view of the Bristol city skyline"></div>
  <div class="badges">
    <span class="badge" style="width:52px;height:52px"></span>
    <span class="badge" style="width:150px;height:46px"></span>
    <span class="badge" style="width:90px;height:46px"></span>
    <span class="badge" style="width:190px;height:40px"></span>
  </div>
  <h3 class="col-title" style="left:350px">Contact Details</h3>
  <h3 class="col-title" style="left:612px">Contact Us</h3>
  <ul class="contact-list">
    <li><svg width="14" height="18" viewBox="0 0 14 18"><path d="M7 0a7 7 0 0 0-7 7c0 5 7 11 7 11s7-6 7-11a7 7 0 0 0-7-7zm0 10a3 3 0 1 1 0-6 3 3 0 0 1 0 6z" fill="#fff"/></svg><span class="label">Address:</span><span>12 Harbour Row<br>Avonmead, Bristol<br>Lorem Ipsum Dolor</span></li>
    <li><svg width="14" height="18" viewBox="0 0 14 18"><path d="M3 1l3 4-2 2c1 2 3 4 5 5l2-2 3 3-2 3C6 16 0 9 1 3z" fill="#fff"/></svg><span class="label">Phone:</span><span>+44 (0)117 000 0000</span></li>
    <li><svg width="16" height="12" viewBox="0 0 16 12"><rect width="16" height="12" fill="#fff"/><path d="M0 0l8 7 8-7" stroke="#1f4a5f" fill="none"/></svg><span class="label" style="width:42px">Email:</span><span>info@thornbury.example</span></li>
  </ul>
  <div class="socials"><span></span><span></span><span></span><span></span></div>
  <div class="field" style="top:248px">Name :</div>
  <div class="field" style="top:298px">Email :</div>
  <div class="field" style="top:348px">Phone :</div>
  <div class="field" style="top:398px;height:82px">Message :</div>
  <div class="submit">Submit</div>
  <div class="map" role="img" aria-label="Street map showing the office location"></div>
  <div class="map-brand"><span class="brand-mark"></span><span class="brand-name">Thornbury Lettings Managment Ltd</span></div>
  <div class="map-link">View Larger Map &#8250;</div>
  <div class="copyright">Copyright @thornbury.example, All rights reserved.</div>
</section>

</body>
</html>
```